Loanvista wedsite and logo refresh

We are looking for someone to refresh the look and feel of Loanvista.co.nz we are moving it towards a more traditional brokerage.

Target Market(s)

30 to 55 year old professionals

Coding

Coded - Design and coding required

Number of Pages Required

3 page

Requirements
Nice to have
• we are needing a modern professional look

```html
<!DOCTYPE html>
<html lang="en">
<head>
<meta charset="utf-8">
<title>Loanvista – Find and Compare Rates</title>
<link href="https://fonts.googleapis.com/css2?family=Oswald:wght@300;400;500&family=Roboto:wght@400;500&display=swap" rel="stylesheet">
<style>
:root{
  --orange:#e8461e;
  --orange-band:#ef5b34;
  --ink:#1c1c1c;
  --text:#777;
  --line:#e2e2e2;
  --white:#fff;
  --footer:#202020;
  --plum:#5b3f4f;
  --gold:#f2b31b;
  --forest:#2d5d3d;
  --teal:#1aa5a8;
}
*{box-sizing:border-box;margin:0;padding:0}
html,body{width:1200px;height:4046px;overflow:hidden}
body{position:relative;background:var(--white);font-family:'Roboto',Arial,sans-serif;color:var(--ink)}
.abs{position:absolute}
.btn{position:absolute;display:flex;align-items:center;justify-content:center;gap:8px;background:var(--orange);color:var(--white);font:500 14px 'Roboto',Arial,sans-serif;text-transform:uppercase;letter-spacing:.2px}
.btn svg{width:14px;height:14px}
.section-title{position:absolute;left:0;width:1200px;text-align:center;font:400 47px 'Oswald',sans-serif;text-transform:uppercase;letter-spacing:-.5px;color:var(--ink)}
.rule{position:absolute;left:576px;width:48px;height:3px;background:var(--orange)}
.lead{position:absolute;left:0;width:1200px;text-align:center;font-size:13.5px;color:var(--text)}

/* hero */
.hero{position:absolute;left:0;top:0;width:1200px;height:671px;background:linear-gradient(100deg,#1d2430 0%,#3a3f47 38%,#6b6358 62%,#453f3a 100%)}
.hero-shade{position:absolute;inset:0;background:linear-gradient(90deg,rgba(10,14,20,.55),rgba(10,14,20,.1) 70%)}
.brand{position:absolute;left:144px;top:32px;font:300 56px 'Oswald',sans-serif;color:var(--white);letter-spacing:-1px;line-height:1}
.nav a{position:absolute;top:55px;color:var(--white);font-size:14px;text-decoration:none;font-weight:500}
.nav .active:after{content:"";position:absolute;left:0;right:0;bottom:-9px;height:2px;background:var(--orange)}
.flag{position:absolute;left:759px;top:58px;width:22px;height:13px}
.login{left:806px;top:47px;width:87px;height:35px}
.signup{position:absolute;left:902px;top:47px;width:154px;height:35px;border:1.5px solid var(--white);color:var(--white);font:500 14px 'Roboto',sans-serif;display:flex;align-items:center;justify-content:center}
.headline{position:absolute;left:141px;top:226px;font:400 76px/77px 'Oswald',sans-serif;color:var(--white);text-transform:uppercase;letter-spacing:-1.5px}
.hero-cta{left:144px;top:496px;width:241px;height:49px}
.dots{position:absolute;left:1128px;top:361px;width:6px}
.dots span{display:block;width:6px;height:6px;border-radius:50%;background:var(--white);margin-bottom:12px}
.dots span.on{background:var(--orange)}

/* rates */
.rate{position:absolute;top:895px;width:200px;text-align:center}
.rate .ring{display:block;margin:0 auto;width:138px;height:138px}
.rate p{margin-top:24px;font:500 14px/19px 'Roboto',sans-serif;text-transform:uppercase}
.more-rates{left:463px;top:1148px;width:274px;height:47px}

/* about */
.about-photo{position:absolute;left:0;top:1294px;width:600px;height:550px;background:linear-gradient(120deg,#d8d2c6 0%,#efe9de 40%,#b79a78 75%,#8a6a48 100%)}
.about-card{position:absolute;left:455px;top:1340px;width:600px;height:455px;background:var(--white);box-shadow:0 2px 12px rgba(0,0,0,.14)}
.about-card h2{position:absolute;left:62px;top:46px;font:400 44px 'Oswald',sans-serif;letter-spacing:-.5px}
.about-card .rule{left:62px;top:120px}
.about-card p{position:absolute;left:62px;top:160px;width:482px;font-size:13px;line-height:26.5px;color:var(--text)}
.about-card .btn{left:62px;top:348px;width:152px;height:49px}

/* why */
.why-card{position:absolute;width:216px;height:273px;background:var(--white);border:1px solid #f3c7b9;border-bottom:4px solid #f8b8a4;text-align:center}
.why-card svg{display:block;margin:26px auto 0;width:60px;height:64px}
.why-card h3{margin-top:18px;font:500 18px/21px 'Roboto',sans-serif;color:var(--ink)}
.why-card p{margin:14px 14px 0;font-size:12px;line-height:21px;color:var(--text)}
.get-started{left:512px;top:2538px;width:176px;height:47px}

/* blog */
.blog-band{position:absolute;left:0;top:2673px;width:1200px;height:545px;background:linear-gradient(90deg,#f06039 0%,#ef5a33 60%,#f26b44 100%)}
.blog-band .section-title{top:96px;color:var(--white)}
.blog-band .rule{top:147px;background:var(--white)}
.post{position:absolute;top:203px;width:278px;height:342px;background:var(--white)}
.post .thumb{height:162px}
.post .date{position:absolute;left:23px;top:177px;width:48px;height:46px;background:var(--orange);color:var(--white);text-align:center;font:500 21px/22px 'Roboto',sans-serif;padding-top:3px}
.post .date small{display:block;font:400 14px/15px 'Roboto',sans-serif}
.post h4{position:absolute;left:83px;top:182px;width:180px;font:500 14.5px/19px 'Roboto',sans-serif;color:var(--ink)}
.post p{position:absolute;left:23px;top:241px;width:240px;font-size:11.5px;line-height:17.5px;color:var(--text)}
.post .read{position:absolute;left:23px;top:306px;font:500 12.5px 'Roboto',sans-serif;color:var(--orange)}

/* contact */
.contact{position:absolute;left:0;top:3218px;width:1200px;height:685px;background:linear-gradient(180deg,#f7f6f5 0%,#fbfbfb 45%,#f1efed 100%)}
.field{position:absolute;background:var(--white);border:1px solid #dcdcdc;font-size:13px;color:#444;padding:20px 0 0 22px}
.submit{left:512px;top:3776px;width:176px;height:47px}

/* footer */
.footer{position:absolute;left:0;top:3903px;width:1200px;height:143px;background:var(--footer)}
.footer nav a{position:absolute;top:43px;color:var(--white);font:500 14px 'Roboto',sans-serif;text-decoration:none}
.footer .copy{position:absolute;left:144px;top:83px;color:#ddd;font-size:12px}
.social{position:absolute;top:46px;width:51px;height:51px;border:2px solid var(--white);border-radius:50%}
</style>
</head>
<body>

<header class="hero">
  <div class="abs" role="img" aria-label="Photo of a smiling couple reviewing loan documents at a table" style="inset:0"></div>
  <div class="hero-shade"></div>
  <div class="brand">LOANVISTA</div>
  <nav class="nav">
    <a class="active" href="#" style="left:488px">SERVICES</a>
    <a href="#" style="left:587px">ABOUT</a>
    <a href="#" style="left:666px">CONTACT</a>
  </nav>
  <svg class="flag" viewBox="0 0 22 13" aria-label="Language: English">
    <rect width="22" height="13" fill="#23347a"/>
    <path d="M0 0L22 13M22 0L0 13" stroke="#fff" stroke-width="3"/>
    <path d="M0 0L22 13M22 0L0 13" stroke="#c8102e" stroke-width="1"/>
    <path d="M11 0v13M0 6.5h22" stroke="#fff" stroke-width="4"/>
    <path d="M11 0v13M0 6.5h22" stroke="#c8102e" stroke-width="2"/>
  </svg>
  <svg class="abs" style="left:784px;top:62px" width="7" height="5" viewBox="0 0 7 5"><path d="M0 0h7L3.5 5z" fill="#fff"/></svg>
  <a class="btn login" href="#">LOGIN</a>
  <a class="signup" href="#">SIGN UP FOR FREE</a>
  <h1 class="headline">No obligations<br>No fees<br>No worries</h1>
  <a class="btn hero-cta" href="#">Find and compare rates
    <svg viewBox="0 0 14 14"><circle cx="7" cy="7" r="7" fill="#fff"/><path d="M5.5 4l3 3-3 3" stroke="#e8461e" stroke-width="2" fill="none"/></svg></a>
  <div class="dots"><span></span><span></span><span class="on"></span><span></span><span></span></div>
</header>

<section class="rates">
  <h2 class="section-title" style="top:744px">Find and compare rates</h2>
  <div class="rule" style="top:819px"></div>

  <div class="rate" style="left:112px">
    <svg class="ring" viewBox="0 0 138 138"><circle cx="69" cy="69" r="67" fill="none" stroke="var(--plum)" stroke-width="4"/>
      <path d="M42 70L69 46l27 24h-7v22H76V78H62v14H49V70z" fill="var(--plum)"/><rect x="82" y="48" width="7" height="12" fill="var(--plum)"/></svg>
    <p>Mortgage rates</p>
  </div>
  <div class="rate" style="left:305px">
    <svg class="ring" viewBox="0 0 138 138"><circle cx="69" cy="69" r="67" fill="none" stroke="var(--gold)" stroke-width="4"/>
      <circle cx="69" cy="57" r="12" fill="var(--gold)"/><path d="M46 92c0-14 10-21 23-21s23 7 23 21z" fill="var(--gold)"/></svg>
    <p>Personal finance</p>
  </div>
  <div class="rate" style="left:500px">
    <svg class="ring" viewBox="0 0 138 138"><circle cx="69" cy="69" r="67" fill="none" stroke="var(--forest)" stroke-width="4"/>
      <path d="M50 66l6-17h26l6 17h4v20h-6v6h-9v-6H59v6h-9v-6h-6V66z" fill="var(--forest)"/>
      <path d="M58 64l4-10h14l4 10z" fill="#fff"/><circle cx="53" cy="75" r="4" fill="#fff"/><circle cx="85" cy="75" r="4" fill="#fff"/></svg>
    <p>Vehicle finance</p>
  </div>
  <div class="rate" style="left:693px">
    <svg class="ring" viewBox="0 0 138 138"><circle cx="69" cy="69" r="67" fill="none" stroke="var(--orange)" stroke-width="4"/>
      <path d="M52 40h24l12 12v46H52z" fill="none" stroke="var(--orange)" stroke-width="4"/><path d="M76 40v12h12" fill="none" stroke="var(--orange)" stroke-width="4"/>
      <path d="M60 64h20M60 73h20M60 82h20" stroke="var(--orange)" stroke-width="4"/></svg>
    <p>Business &amp; asset<br>finance</p>
  </div>
  <div class="rate" style="left:886px">
    <svg class="ring" viewBox="0 0 138 138"><circle cx="69" cy="69" r="67" fill="none" stroke="var(--teal)" stroke-width="4"/>
      <rect x="52" y="40" width="34" height="58" fill="var(--teal)"/>
      <g fill="#fff"><rect x="57" y="46" width="5" height="5"/><rect x="66.5" y="46" width="5" height="5"/><rect x="76" y="46" width="5" height="5"/>
      <rect x="57" y="56" width="5" height="5"/><rect x="66.5" y="56" width="5" height="5"/><rect x="76" y="56" width="5" height="5"/>
      <rect x="57" y="66" width="5" height="5"/><rect x="66.5" y="66" width="5" height="5"/><rect x="76" y="66" width="5" height="5"/>
      <rect x="57" y="76" width="5" height="5"/><rect x="66.5" y="76" width="5" height="5"/><rect x="76" y="76" width="5" height="5"/>
      <rect x="65" y="87" width="8" height="11"/></g></svg>
    <p>Commercial<br>finance</p>
  </div>

  <a class="btn more-rates" href="#">View more compare rates
    <svg viewBox="0 0 14 14"><circle cx="7" cy="7" r="7" fill="#fff"/><path d="M5.5 4l3 3-3 3" stroke="#e8461e" stroke-width="2" fill="none"/></svg></a>
</section>

<section class="about">
  <div class="about-photo" role="img" aria-label="Photo of a family carrying moving boxes into their new home"></div>
  <div class="about-card">
    <h2>ABOUT LOANVISTA?</h2>
    <div class="rule"></div>
    <p>Lorem ipsum dolor sit amet, consectetur adipiscing elit, sed do eiusmod tempor incididunt ut labore et dolore magna is ipsum suspendisse ultrices gravidaisus commodo viverra maecenas accumsan lacus vel facilisis. Lorem ipsum dolor sit amet, consectetur adipiscing elit, sed do eiusmod tempor incididunt ut labore et dolore magna is ipsum suspendisse ultrices gravidaiscommodo viverra maecenas accumsan lacfacilisim ipsum dolor sitnsectetur.</p>
    <a class="btn" href="#">Read more
      <svg viewBox="0 0 14 14"><circle cx="7" cy="7" r="7" fill="#fff"/><path d="M5.5 4l3 3-3 3" stroke="#e8461e" stroke-width="2" fill="none"/></svg></a>
  </div>
</section>

<section class="why">
  <h2 class="section-title" style="top:1950px">Why Loanvista?</h2>
  <div class="rule" style="top:2026px"></div>
  <p class="lead" style="top:2063px">Lorem ipsum dolor sit amsectetur adipiscing elit sed do eiusmod tempor incididunt</p>

  <div class="why-card" style="left:144px;top:2153px">
    <svg viewBox="0 0 60 64" fill="none" stroke="var(--orange)" stroke-width="2.2">
      <circle cx="30" cy="22" r="19"/><circle cx="30" cy="22" r="13"/>
      <path d="M30 14l2.5 5 5.5.8-4 3.9 1 5.4-5-2.6-5 2.6 1-5.4-4-3.9 5.5-.8z"/>
      <path d="M18 37l-7 20 7-3 4 6 6-17M42 37l7 20-7-3-4 6-6-17"/></svg>
    <h3>Great rates &amp;<br>Incentives</h3>
    <p>Lorem ipsum dolor simonsectetur adipiscing elid do eiusmod tempor incididunt laboreet dolore</p>
  </div>
  <div class="why-card" style="left:375px;top:2180px">
    <svg viewBox="0 0 60 64" fill="none" stroke="var(--orange)" stroke-width="2.2">
      <path d="M30 62C18 46 10 36 10 24a20 20 0 0 1 40 0c0 12-8 22-20 38z"/>
      <circle cx="30" cy="24" r="12"/><path d="M30 17v7l5 4"/></svg>
    <h3>Any Time<br>Any where</h3>
    <p>Lorem ipsum dolor simonsectetur adipiscing elid do eiusmod tempor incididunt laboreet dolore</p>
  </div>
  <div class="why-card" style="left:608px;top:2153px">
    <svg viewBox="0 0 60 64" fill="none" stroke="var(--orange)" stroke-width="2.2">
      <path d="M2 32c8-12 18-18 28-18s20 6 28 18c-8 12-18 18-28 18S10 44 2 32z"/>
      <circle cx="30" cy="32" r="13"/><rect x="25" y="31" width="10" height="8"/><path d="M27 31v-3a3 3 0 0 1 6 0v3"/></svg>
    <h3>Privacy is<br>Important</h3>
    <p>Lorem ipsum dolor simonsectetur adipiscing elid do eiusmod tempor incididunt laboreet dolore</p>
  </div>
  <div class="why-card" style="left:839px;top:2180px">
    <svg viewBox="0 0 60 64" fill="none" stroke="var(--orange)" stroke-width="2.2">
      <rect x="6" y="30" width="11" height="26"/>
      <path d="M17 33l10-12 4-12c4 0 6 3 5 8l-2 9h14c3 0 5 3 4 6l-1 2c2 1 2 4 0 6 2 1 2 4 0 6 1 2 0 5-3 5H17"/>
      <path d="M40 39h12M41 45h11M40 51h10"/></svg>
    <h3>No Fees<br>No Obligations</h3>
    <p>Lorem ipsum dolor simonsectetur adipiscing elid do eiusmod tempor incididunt laboreet dolore</p>
  </div>

  <a class="btn get-started" href="#">Get started
    <svg viewBox="0 0 14 14"><circle cx="7" cy="7" r="7" fill="#fff"/><path d="M5.5 4l3 3-3 3" stroke="#e8461e" stroke-width="2" fill="none"/></svg></a>
</section>

<section class="blog-band">
  <h2 class="section-title">Blog posts</h2>
  <div class="rule"></div>

  <article class="post" style="left:154px">
    <div class="thumb" role="img" aria-label="Photo of an adviser meeting a couple at a desk" style="background:linear-gradient(135deg,#9a8f84,#e4ddd3 55%,#6d6660)"></div>
    <div class="date">02<small>JAN</small></div>
    <h4>Lorem ipsum dolor sit amonsectetur adipiscing</h4>
    <p>Sed ut perspiciatis unde omnis iste natus error sit voluptatem accusantilo laudantium, totam rem aperiam eaque ipsa</p>
    <a class="read">READ MORE</a>
  </article>
  <article class="post" style="left:460px">
    <div class="thumb" role="img" aria-label="Photo of a family sitting together on the floor of a bright living room" style="background:linear-gradient(135deg,#e9e6e1,#cfc6bb 50%,#f1efeb)"></div>
    <div class="date">02<small>JAN</small></div>
    <h4>Lorem ipsum dolor sit amonsectetur adipiscing</h4>
    <p>Sed ut perspiciatis unde omnis iste natus error sit voluptatem accusantilo laudantium, totam rem aperiam eaque ipsa</p>
    <a class="read">READ MORE</a>
  </article>
  <article class="post" style="left:765px">
    <div class="thumb" role="img" aria-label="Photo of hands signing a loan contract beside a laptop" style="background:linear-gradient(135deg,#3b3e48,#8f8a86 50%,#d9d5cf)"></div>
    <div class="date">02<small>JAN</small></div>
    <h4>Lorem ipsum dolor sit amonsectetur adipiscing</h4>
    <p>Sed ut perspiciatis unde omnis iste natus error sit voluptatem accusantilo laudantium, totam rem aperiam eaque ipsa</p>
    <a class="read">READ MORE</a>
  </article>
</section>

<section class="contact">
  <h2 class="section-title" style="top:92px">Get in touch</h2>
  <div class="rule" style="top:168px"></div>
  <p class="lead" style="top:205px">Lorem ipsum dolor sit amsectetur adipiscing elit sed do eiusmod tempor incididunt</p>
</section>
<form>
  <div class="field" style="left:232px;top:3498px;width:361px;height:53px">First Name</div>
  <div class="field" style="left:605px;top:3498px;width:360px;height:53px">Last Name</div>
  <div class="field" style="left:232px;top:3562px;width:361px;height:54px">Email address</div>
  <div class="field" style="left:605px;top:3562px;width:360px;height:54px">Phone Number</div>
  <div class="field" style="left:232px;top:3628px;width:733px;height:115px">Message</div>
  <a class="btn submit" href="#">Submit mesage
    <svg viewBox="0 0 14 14"><circle cx="7" cy="7" r="7" fill="#fff"/><path d="M5.5 4l3 3-3 3" stroke="#e8461e" stroke-width="2" fill="none"/></svg></a>
</form>

<footer class="footer">
  <nav>
    <a href="#" style="left:144px">HOME</a>
    <a href="#" style="left:217px">SERVICES</a>
    <a href="#" style="left:316px">ABOUT</a>
    <a href="#" style="left:394px">CONTACT</a>
    <a href="#" style="left:490px">TERMS AND PRIVACY</a>
  </nav>
  <p class="copy">© 2020 Loanvista.All Rights Reserved &nbsp;|&nbsp; Privacy Policy</p>
  <span class="social" style="left:813px" aria-label="Social link"></span>
  <span class="social" style="left:876px" aria-label="Social link"></span>
  <span class="social" style="left:938px" aria-label="Social link"></span>
  <span class="social" style="left:1003px" aria-label="Social link"></span>
</footer>

</body>
</html>
```